Brenmoor Group needs a business card

I would like the card to be simple but modern and elegant.
I like black and white.
or black and gold.
we are a private finance lender and also are involved in property and property developments.

please look at the business card photos i provided i would like B.G only one one side and all the other details on the other side use fonts that tie in with my theme.

Industry/Entity Type

Finance

Contact Information for Business Card

Brenmoor Group (B.G) Callum Brenmoor M: 0418396152 E: callumbren@quivomail.com

Font styles to use
Other font styles liked:
• Use fonts that would reflect our business

Colors
000000
ffffff

Requirements
Must have
• one side of details
• other side has either B.G or Brenmoor Group like in the photos provided

```html
<!DOCTYPE html>
<html lang="en">
<head>
<meta charset="utf-8">
<title>Brenmoor Group — Business Card</title>
<link rel="stylesheet" href="https://fonts.googleapis.com/css2?family=Lato:wght@300;400&display=swap">
<style>
  :root {
    --backdrop: #ece9e4;
    --card-gold: #f3c800;
    --card-edge: #000000;
    --ink: #111111;
  }
  * { box-sizing: border-box; margin: 0; padding: 0; }
  html, body {
    width: 1200px;
    height: 512px;
    overflow: hidden;
    background: var(--backdrop);
  }
  .canvas {
    width: 1200px;
    height: 512px;
    display: flex;
    align-items: center;
    justify-content: center;
    gap: 80px;
  }
  .card {
    position: relative;
    width: 500px;
    height: 300px;
    background: var(--card-gold);
    border: 12px solid var(--card-edge);
    color: var(--ink);
    font-family: "Lato", "Gill Sans", sans-serif;
    font-weight: 300;
  }
  .card-front .company {
    position: absolute;
    top: 9px;
    left: 12px;
    font-size: 15px;
    white-space: nowrap;
  }
  .card-front .details {
    position: absolute;
    top: 116px;
    left: 160px;
    width: 240px;
    text-align: center;
  }
  .card-front .name {
    font-size: 20px;
    padding-bottom: 4px;
    border-bottom: 1.5px solid var(--ink);
    margin-bottom: 6px;
    white-space: nowrap;
  }
  .card-front .contact {
    font-size: 15px;
    line-height: 1.3;
    white-space: nowrap;
  }
  .card-back .monogram {
    position: absolute;
    top: 62px;
    left: 0;
    right: 0;
    padding-left: 70px;
    text-align: center;
    font-size: 64px;
    font-weight: 300;
    letter-spacing: 4px;
    line-height: 1;
  }
</style>
</head>
<body>
  <main class="canvas">
    <section class="card card-front" aria-label="Card front">
      <p class="company">Brenmoor Group (B.G)</p>
      <div class="details">
        <p class="name">Callum Brenmoor</p>
        <p class="contact">M: 0418396152</p>
        <p class="contact">E: callumbren@quivomail.com</p>
      </div>
    </section>
    <section class="card card-back" aria-label="Card back">
      <p class="monogram">B.G</p>
    </section>
  </main>
</body>
</html>
```